Carers Together Circle Business Cards

The Carers Together Circle provides Continuing Professional Development opportunities to Nurses both online and via exciting Travel adventures to fabulous destinations worldwide.

We require business cards for our staff and at a minimum, the card will need:

Full Name
Position
p 07 5928 6247
m 0411 222 333 (optional)
e info@wardlinkgroup.example
w www.wardlinkgroup.example

I will need a template so that I can edit different employee details as they come and go.

Here is our website - www.wardlinkgroup.example, so you can see what we are about.

I have attached our logo and if you need to know these are the colours we use on our website - orange #F4701D, Purple #6A136A and green #63AB32

Let me know if you need further details, I look forward to seeing your designs.

Cheers,
Marta.

Industry/Entity Type

Business

```html
<!DOCTYPE html>
<html lang="en">
<head>
<meta charset="utf-8">
<title>Carers Together Circle – Business Cards</title>
<link href="https://fonts.googleapis.com/css2?family=Questrial&display=swap" rel="stylesheet">
<style>
  :root {
    --purple: #722283;
    --purple-deep: #5e1a6e;
    --purple-light: #8a3a9b;
    --orange: #f4701d;
    --ink: #4a4a4a;
    --white: #ffffff;
    --backdrop: #ecebe8;
  }
  * { box-sizing: border-box; margin: 0; padding: 0; }
  html, body {
    width: 1200px; height: 1024px; overflow: hidden;
    background: var(--backdrop);
    font-family: "Questrial", "Century Gothic", sans-serif;
  }
  .sheet {
    width: 1200px; height: 1024px;
    display: flex; flex-direction: column; align-items: center;
    justify-content: center; gap: 40px;
  }
  .card {
    position: relative;
    width: 840px; height: 480px;
    border-radius: 6px; overflow: hidden;
    box-shadow: 0 6px 18px rgba(0,0,0,0.12);
  }

  /* Front */
  .card--front { background: var(--white); }
  .front__panel {
    position: absolute; top: 0; right: 0; bottom: 0; width: 42%;
    background: linear-gradient(160deg, var(--purple-light) 0%, var(--purple) 45%, var(--purple-deep) 100%);
  }
  .front__brand {
    position: absolute; top: 60px; right: 52px;
    display: flex; align-items: flex-start; gap: 16px;
  }
  .brand-dot {
    width: 18px; height: 18px; border-radius: 50%;
    background: var(--white); margin-top: 10px; flex: none;
  }
  .brand-name {
    color: var(--white); font-size: 38px; line-height: 1.05;
    font-weight: 400; text-transform: lowercase; letter-spacing: 0.5px;
  }
  .front__details {
    position: absolute; left: 56px; bottom: 64px;
  }
  .person-name {
    color: var(--purple); font-weight: 700; font-size: 26px;
    letter-spacing: 1.5px; text-transform: uppercase;
  }
  .person-role {
    color: var(--orange); font-size: 20px; margin-top: 4px;
  }
  .contact-list { list-style: none; margin-top: 36px; }
  .contact-list li {
    color: var(--ink); font-size: 19px; line-height: 1.6;
  }
  .contact-list .label { color: var(--purple); font-weight: 700; }

  /* Back */
  .card--back {
    background: linear-gradient(150deg, var(--purple-light) 0%, var(--purple) 40%, var(--purple-deep) 100%);
  }
  .back__brand {
    position: absolute; top: 50%; left: 50%;
    transform: translate(-50%, -50%);
    display: flex; align-items: flex-start; gap: 18px;
  }
  .back__brand .brand-name { font-size: 52px; }
  .back__brand .brand-dot { width: 22px; height: 22px; margin-top: 16px; }
  .back__url {
    position: absolute; left: 48px; bottom: 40px;
    color: var(--white); font-size: 17px; letter-spacing: 0.5px; opacity: 0.9;
  }
</style>
</head>
<body>
<main class="sheet">
  <section class="card card--front" aria-label="Business card front">
    <div class="front__panel"></div>
    <div class="front__brand">
      <span class="brand-dot"></span>
      <p class="brand-name">carers<br>together<br>circle</p>
    </div>
    <div class="front__details">
      <p class="person-name">Daniel Reyes</p>
      <p class="person-role">Position</p>
      <ul class="contact-list">
        <li><span class="label">p</span> : 07 5928 6247</li>
        <li><span class="label">m</span> : 0411 222 333 (optional)</li>
        <li><span class="label">e</span> : info@wardlinkgroup.example</li>
        <li><span class="label">w</span> : www.wardlinkgroup.example</li>
      </ul>
    </div>
  </section>

  <section class="card card--back" aria-label="Business card back">
    <div class="back__brand">
      <span class="brand-dot"></span>
      <p class="brand-name">carers<br>together<br>circle</p>
    </div>
    <p class="back__url">www.wardlinkgroup.example</p>
  </section>
</main>
</body>
</html>
```